HVAC company business card design

We need a business card design for a HVAC company. The design must look professional. Both sides will be used. The total data to be on the business card is
Name
Position
Email
Direct Phone/Moile Phone
Company Contacts /Address, Phone, Fax, web)
All data will be submit once the design is confirmed. For generic purposes use;
Emre Toksoy
Managing Director
+902324815263 (Mobile)
4712 Sokak No: 9 KBSE Yenikent IZMIR TURKEY
Tel: +902324815263 Fax : +902324815269
www.luvon.com.tr

Target Market(s)

HVAC

Industry/Entity Type

Business

Contact Information for Business Card

The total data to be on the business card is
Name
Position
Email
Direct Phone/Moile Phone
Emre Toksoy
Managing Director
+902324815263 (Mobile)
www.luvon.com.tr
The BC will use both sides of the card. The front will include the full logo and the details for the business card holder. The business card can be divided into vertical/horizontal or to a special shape. The common data like the company address/phone/fax should be indicated elsewehere. The back can contain some part or the whole logo and must contain the web address.

Font styles to use
Serif
Sans Serif

Colors
0355a3
cfdfed

Requirements
Should not have
• Please be careful with the fonts, it shouldnt be too small or too big and must not interfere with the logo fonts. If you need to use a curvy shape please do not use as the logo is already curvy or use the curves from the logo (if it looks good, otherwise forget it)
• We are not in favor of pictograms, only if they are perfect use them.

```html
<!DOCTYPE html>
<html lang="en">
<head>
<meta charset="utf-8">
<title>Luvon business card</title>
<link rel="stylesheet" href="https://fonts.googleapis.com/css2?family=Questrial&display=swap">
<style>
  :root {
    --page: #dcdcec;
    --navy: #3c4660;
    --blue: #2a62c4;
    --blue-light: #4a8fe0;
    --paper: #f2f4f8;
    --ink: #3a4258;
    --silver: #c9ccd4;
    --silver-light: #e4e6ec;
    --white: #ffffff;
  }
  * { box-sizing: border-box; margin: 0; padding: 0; }
  html, body { width: 1200px; height: 906px; overflow: hidden; }
  body {
    background: var(--page);
    font-family: "Questrial", sans-serif;
    position: relative;
  }
  .card {
    position: absolute;
    width: 620px;
    height: 360px;
    overflow: hidden;
    box-shadow: 0 10px 30px rgba(40, 40, 80, 0.18);
  }

  /* back side */
  .card-back { left: 110px; top: 50px; background: var(--navy); }
  .back-decor {
    position: absolute; left: 0; top: 0; width: 230px; height: 360px;
    background: linear-gradient(135deg, var(--silver-light) 0%, var(--silver) 55%, var(--blue) 100%);
  }
  .back-brand {
    position: absolute; left: 300px; top: 140px;
    display: flex; align-items: center; gap: 16px;
  }
  .brand-dot { width: 44px; height: 44px; border-radius: 50%; background: var(--blue); flex: none; }
  .back-brand .brand-name { color: var(--white); font-size: 56px; letter-spacing: 4px; line-height: 1; }
  .back-web {
    position: absolute; right: 40px; bottom: 34px;
    color: var(--white); font-size: 16px; letter-spacing: 1px;
  }

  /* front side */
  .card-front { left: 470px; top: 480px; background: var(--paper); }
  .front-brand {
    position: absolute; left: 50px; top: 142px;
    display: flex; align-items: center; gap: 14px;
  }
  .front-brand .brand-name { color: var(--navy); font-size: 50px; letter-spacing: 4px; line-height: 1; }
  .divider {
    position: absolute; left: 350px; top: 30px; width: 1px; height: 260px;
    background: linear-gradient(var(--paper), #c6cad6, var(--paper));
  }
  .holder { position: absolute; left: 372px; top: 40px; color: var(--ink); }
  .holder-name { color: var(--blue); font-size: 19px; letter-spacing: 0.5px; }
  .holder-title { font-size: 14px; margin-top: 3px; }
  .contact-list { list-style: none; margin-top: 14px; }
  .contact-list li {
    display: flex; align-items: center; gap: 10px;
    font-size: 14px; line-height: 22px;
  }
  .icon {
    width: 16px; height: 16px; border-radius: 3px; background: var(--blue);
    display: inline-flex; align-items: center; justify-content: center; flex: none;
  }
  .address { font-size: 14px; line-height: 20px; margin-top: 12px; }
  .band {
    position: absolute; left: 0; bottom: 0; width: 620px; height: 26px;
  }
</style>
</head>
<body>

  <section class="card card-back" aria-label="Card back">
    <div class="back-decor" role="img" aria-label="Decorative silver and blue graphic area"></div>
    <div class="back-brand">
      <span class="brand-dot"></span>
      <span class="brand-name">LUVON</span>
    </div>
    <p class="back-web">www.luvon.com.tr</p>
  </section>

  <section class="card card-front" aria-label="Card front">
    <div class="front-brand">
      <span class="brand-dot"></span>
      <span class="brand-name">LUVON</span>
    </div>

    <div class="divider"></div>

    <div class="holder">
      <p class="holder-name">EMRE TOKSOY</p>
      <p class="holder-title">Managing Director</p>
      <ul class="contact-list">
        <li><span class="icon"><svg width="10" height="12" viewBox="0 0 10 12"><rect x="2" y="0.5" width="6" height="11" rx="1" fill="none" stroke="#fff" stroke-width="1.4"/></svg></span>+902324815263</li>
        <li><span class="icon"><svg width="12" height="12" viewBox="0 0 12 12"><path d="M2 1 L4.5 1 L5.5 4 L4 5 C5 7 6 8 7 8.5 L8 7 L11 8 L11 10.5 C6 11 1 6 2 1Z" fill="#fff"/></svg></span>+902324815269</li>
        <li><span class="icon"><svg width="12" height="12" viewBox="0 0 12 12"><rect x="1" y="4" width="10" height="6" fill="none" stroke="#fff" stroke-width="1.3"/><rect x="3" y="1" width="6" height="3" fill="#fff"/></svg></span>+902324815271</li>
        <li><span class="icon"><svg width="12" height="10" viewBox="0 0 12 10"><rect x="0.8" y="0.8" width="10.4" height="8.4" fill="none" stroke="#fff" stroke-width="1.3"/><path d="M1 1 L6 5.5 L11 1" fill="none" stroke="#fff" stroke-width="1.3"/></svg></span>info@luvon.com.tr</li>
        <li><span class="icon"><svg width="12" height="12" viewBox="0 0 12 12"><circle cx="6" cy="6" r="5" fill="none" stroke="#fff" stroke-width="1.2"/><path d="M1 6 H11 M6 1 C3 4 3 8 6 11 C9 8 9 4 6 1" fill="none" stroke="#fff" stroke-width="1"/></svg></span>www.luvon.com.tr</li>
      </ul>
      <p class="address">4712 Sokak No: 9<br>KBSE Yenikent IZMIR TURKEY</p>
    </div>

    <svg class="band" viewBox="0 0 620 26" preserveAspectRatio="none" aria-hidden="true">
      <polygon points="0,26 0,14 360,14 372,0 620,0 620,26" fill="var(--blue)"/>
      <polygon points="0,26 0,14 360,14 352,26" fill="var(--navy)"/>
    </svg>
  </section>

</body>
</html>
```